Real Estate "For Sale" Sign for construction company

We need a sign that we can use to hang on a post and place on the road when we sell a property. The sign will be simple and will need to mainly feature our logo (files attached), as well as the words "For Sale", and then our phone number "(555) 617 3489". The sign will hang on a post that'll look something like the attached picture.

Target Market(s)

Home buyers

Industry/Entity Type

Real Estate

Font styles to use
Serif
Sans Serif

Colors
0054AA
0677BA
7BADD7
CADEEF
E8F1F8
0094D4
00A9DD
6FCCEA
C7EBF8
E9F6FB

Requirements
Must have
• For Sale & our phone number

```html
<!DOCTYPE html>
<html lang="en">
<head>
<meta charset="UTF-8">
<title>For Sale Sign – Cedar Hollow Homes</title>
<link href="https://fonts.googleapis.com/css2?family=Montserrat:wght@500;800&display=swap" rel="stylesheet">
<style>
  :root {
    --backdrop: #cfcfcf;
    --sign-white: #f4f4f4;
    --navy: #05388b;
    --sky: #4dbbe8;
    --brand-blue: #0677ba;
    --text-white: #f4f4f4;
    --text-shadow: #0a2458;
  }
  html, body {
    margin: 0;
    padding: 0;
    width: 1200px;
    height: 1200px;
    overflow: hidden;
    background: var(--backdrop);
  }
  .canvas {
    width: 1200px;
    height: 1200px;
    display: flex;
    align-items: center;
    justify-content: center;
  }
  .sign {
    width: 800px;
    height: 1068px;
    display: flex;
    flex-direction: column;
    font-family: "Montserrat", Arial, sans-serif;
  }
  .sign__brand {
    height: 290px;
    background: var(--sign-white);
    display: flex;
    flex-direction: column;
    align-items: center;
    justify-content: center;
    color: var(--brand-blue);
    font-weight: 500;
  }
  .brand-name {
    font-size: 58px;
    letter-spacing: 0.5px;
    line-height: 1;
  }
  .brand-tag {
    margin-top: 18px;
    font-size: 17px;
    letter-spacing: 16px;
    padding-left: 16px;
    line-height: 1;
  }
  .sign__headline {
    height: 620px;
    background: var(--navy);
    display: flex;
    flex-direction: column;
    align-items: center;
    justify-content: center;
    color: var(--text-white);
    font-weight: 800;
    font-size: 222px;
    line-height: 0.98;
    text-shadow: 3px 4px 0 var(--text-shadow);
  }
  .headline-line {
    display: block;
  }
  .sign__contact {
    height: 158px;
    background: var(--sky);
    display: flex;
    align-items: center;
    justify-content: center;
    color: var(--text-white);
    font-weight: 800;
    font-size: 76px;
    letter-spacing: -1px;
    text-shadow: 2px 3px 0 rgba(10, 36, 88, 0.35);
  }
</style>
</head>
<body>
  <main class="canvas">
    <section class="sign">
      <header class="sign__brand">
        <div class="brand-name">Cedar Hollow</div>
        <div class="brand-tag">HOMES</div>
      </header>
      <div class="sign__headline">
        <span class="headline-line">FOR</span>
        <span class="headline-line">SALE</span>
      </div>
      <footer class="sign__contact">(555) 617 3489</footer>
    </section>
  </main>
</body>
</html>
```